Jo & Mira's Homepage Design - Florists

Hello PixelHive,

We’re Jo and Mira and we own a lovely flower shop in Marlow. We’re looking to launch a website that gives our customers all information they need to know about getting in contact with us. In time we hope the website will grow and we will want to add new pages as we go along including ecommerce functionality, so the design will need to allow for this.

The brief:
We are looking for 1 homepage design. We have already had our logo designed, which we’ve attached for you to use. At the moment we’re keen to have a homepage design that showcases six of our most popular bouquets, see attached pictures and our contact details. We are looking for a contemporary design that’s inline with our logo. Please do not use dark background colours, we want a clean, light and simple design that looks fresh, modern and professional. Please remember that the majority of web monitors now use a screen resolution of 1366x768. Therefore please do not design a 800 x 600 homepage.

1. Our logo and icon (See attachments)
2. Potential hero images attached for inspiration. 6 Bouquets attached but dont make it look like a bog standard ecommerce site. You dont have to use the 6 bouquets. Our site is more brand as we dont have ecom functionality yet.
3. Our contact details including:

Name:
Jo and Mira’s (note 1 ‘L’ in Mira’s name, use the logo)

Navigation

Homepage needs to include the following copy
‘Free delivery with all orders”
‘Fresh – 7 days of flower freshness guaranteed’
‘Hand delivered and hand prepared by a professional florist’
Very clear call to action to ‘Order today: 0203 554 2071 or email us (visually a clickable link) today

Payment visuals: show that we accept PAYRO/Cardwell/Northern Swift/Quikpay, with logos

Telephone numbers:
0203 554 2071 (Central London)
0208 417 2359 (Greater London)
01628 570213 (Marlow)
07845 190627 (Mobile)

E-mail address
orders@joandmiras.co.uk (Orders)
CS@joandmiras.co.uk (Customer Service)

Chatterly page link (use CH logo)
http://www.facebook.com/joandmiras

The National Petal Guild logo
Attached should be displayed on the bottom of the homepage somewhere, prefer bottom right.

Other sites we like:
http://www.bloomsbyharriet.com
http://maisondepetale.com
Like the fun of this one - http://www.grandpagoose.co.uk/goto/home

Our logo should be a good guide for how we’d like the overall page to look, please use this as a starter for your designs. Fee; free to submit your designs and I’ll feedback on changes.

We look forward to seeing your designs!

Jo & Mira

Industry/Entity Type

Florist

Requirements
Must have
• Please see the attached brief. Please use our logo and icon in the design.
Should not have
• Do not use dark background colours, it should feel light and fresh.

```html
<!DOCTYPE html>
<html lang="en">
<head>
<meta charset="utf-8">
<title>Jo &amp; Mira's – Florists</title>
<link rel="stylesheet" href="https://fonts.googleapis.com/css2?family=Arimo:wght@400;700&family=Cinzel:wght@400&family=Roboto+Condensed:ital,wght@1,700&display=swap">
<style>
:root{
  --purple:#8b3a98;
  --plum:#5c2a5e;
  --green:#4cb848;
  --red:#e0283e;
  --orange:#e8940f;
  --pink:#ea3a6c;
  --ink:#1e1e1e;
  --grey:#6d6d6d;
  --footer:#f5f3ef;
  --footer-line:#e2ded6;
  --footer-label:#7a7a7a;
  --rule:#d8d8d8;
}
*{box-sizing:border-box;margin:0;padding:0}
html,body{width:913px;height:1200px;overflow:hidden;background:#fff}
body{position:relative;font-family:"Arimo",Arial,sans-serif;color:var(--ink)}
.abs{position:absolute}

.brand{left:112px;top:46px;font-size:36px;color:#333;display:flex;align-items:center;gap:8px;letter-spacing:-1px}
.brand-dot{width:14px;height:14px;border-radius:50%;background:var(--purple)}

.order-box{left:641px;top:11px;width:158px;height:96px;border:1px solid #e2e2e2;text-align:center;padding-top:12px}
.order-title{font-family:"Cinzel",serif;color:var(--purple);font-size:19px;line-height:20px}
.order-phone{font-family:"Roboto Condensed",sans-serif;font-style:italic;font-weight:700;color:var(--green);font-size:16px;margin-top:2px;display:flex;justify-content:center;align-items:center;gap:5px}
.order-email{display:inline-block;margin-top:8px;background:var(--purple);color:#fff;font-weight:700;font-size:13px;padding:5px 9px;text-decoration:none}

.nav-main{left:36px;top:127px;width:841px;height:21px;background:#222;display:flex;justify-content:center;align-items:center}
.nav-main a{color:#fff;font-weight:700;font-size:11.5px;text-decoration:none;padding:0 18px;border-left:1px solid #888;line-height:12px}
.nav-main a:first-child{border-left:0}
.nav-sub{left:36px;top:149px;width:841px;height:21px;display:flex;justify-content:center;align-items:center;background:linear-gradient(#fff,#f4f4f4)}
.nav-sub a{color:var(--green);font-weight:700;font-size:11.5px;text-decoration:none;padding:0 14px;border-left:1px solid #bbb;line-height:12px}
.nav-sub a:first-child{border-left:0}

.hero{left:35px;top:184px;width:842px;height:313px;background:#fff;box-shadow:0 0 30px rgba(120,110,80,.35)}
.hero-photo{left:0;top:0;width:440px;height:313px;background:radial-gradient(ellipse at 48% 42%,#e23a1e 0%,#c62a18 35%,#a8524a 55%,#e9e6e2 72%,#f3f2f0 100%)}
.hero-title{left:427px;top:72px;font-family:"Cinzel",serif;color:var(--red);font-size:38px;line-height:42px}
.hero-sub{left:429px;top:114px;font-family:"Roboto Condensed",sans-serif;font-style:italic;font-weight:700;color:var(--green);font-size:28px}
.hero-points{left:430px;top:161px;font-family:"Cinzel",serif;font-size:11px;color:#333;line-height:18px}
.btn{display:block;background:var(--green);color:#fff;font-weight:700;font-size:13.5px;text-align:center;text-decoration:none;height:25px;line-height:25px;width:107px;text-shadow:0 1px 1px rgba(0,0,0,.25)}
.hero .btn{position:absolute;left:430px;top:216px}
.dots{left:430px;top:268px;display:flex;gap:6px}
.dot{width:18px;height:18px;border-radius:50%;border:3px solid #d3d3d3}
.dot.active{border-color:var(--green)}

.feature-title{font-family:"Cinzel",serif;font-weight:400;color:var(--plum);font-size:21.5px}
.feature-photo{width:197px;height:276px}
.feature-lead{font-size:11.5px;line-height:15px;color:#111;width:176px}
.feature-body{font-size:11.5px;line-height:18px;color:var(--grey);width:180px}

.site-footer{left:36px;top:884px;width:841px;height:270px;background:var(--footer);border:1px solid var(--footer-line)}
.footer-rule{left:0;top:51px;width:839px;height:1px;background:var(--footer-line)}
.footer-head{font-weight:700;font-size:14.5px;top:27px}
.footer-label{font-weight:700;font-size:12.5px;color:var(--footer-label)}
.footer-value{font-weight:700;font-size:12.5px;color:#222;margin-top:3px;margin-bottom:10px}
.social-sq{width:16px;height:16px;background:#4a6cb3;display:inline-block}
.social{display:flex;align-items:center;gap:5px;color:#222;font-size:12px;font-weight:700}
.guild-head{color:var(--orange);font-weight:700;font-size:14.5px;line-height:19px}
.guild-badge{width:178px;height:102px;background:#fff;border:1px solid var(--footer-line);display:flex;align-items:center;justify-content:center}
.guild-mark{width:120px;height:60px;border-radius:50%;background:#f2e6c9}

.pay-head{color:var(--purple);font-weight:700;font-size:12.5px;margin-bottom:7px}
.pay-grid{display:grid;grid-template-columns:100px 100px;gap:6px}
.pay-card{height:24px;background:#fff;border:1px solid var(--footer-line);font-weight:700;font-size:11px;color:#333;display:flex;align-items:center;justify-content:center}

.bottom-rule{left:36px;top:1165px;width:841px;height:1px;background:var(--rule)}
.bottom-links{left:36px;top:1177px;width:841px;text-align:center;font-size:12px;color:#444}
.bottom-links a{color:#444;text-decoration:none;padding:0 6px;border-left:1px solid #777}
.bottom-links a:first-child{border-left:0}
</style>
</head>
<body>

<header>
  <div class="abs brand"><span class="brand-dot"></span>Jo &amp; Mira's</div>
  <div class="abs order-box">
    <div class="order-title">Order Today</div>
    <div class="order-phone">
      <svg width="15" height="11" viewBox="0 0 15 11" aria-hidden="true"><path d="M1 4 Q7.5 -1 14 4 L12 5.5 L10 4 L10 3 Q7.5 2 5 3 L5 4 L3 5.5Z M4 6 L11 6 L13 10.5 L2 10.5Z" fill="#4cb848"/></svg>
      0203 554 2071
    </div>
    <a class="order-email" href="#">or email us today</a>
  </div>
  <nav class="abs nav-main">
    <a href="#">Classic Flowers</a><a href="#">Luxury Bouqets</a><a href="#">Platinum Collection</a><a href="#">Autumn Flowers</a><a href="#">Luxury Roses</a>
  </nav>
  <nav class="abs nav-sub">
    <a href="#">Latest Designs</a><a href="#">Our Favourites</a><a href="#">Delivery Information</a><a href="#">Customer Service</a><a href="#">FAQ</a><a href="#">About Us</a>
  </nav>
</header>

<section class="abs hero">
  <div class="abs hero-photo" role="img" aria-label="Bouquet of red and orange roses on a white table"></div>
  <div class="abs hero-title">Free Delivery</div>
  <div class="abs hero-sub">with all orders</div>
  <div class="abs hero-points">Fresh – 7 days of flower freshness guaranteed<br>Hand delivered and hand prepared by a professional florist</div>
  <a class="btn" href="#">Read more</a>
  <div class="abs dots"><span class="dot"></span><span class="dot active"></span><span class="dot"></span><span class="dot"></span></div>
</section>

<section>
  <h2 class="abs feature-title" style="left:38px;top:528px">Fugit Delicata Ei Mea Laudem</h2>
  <div class="abs feature-photo" style="left:36px;top:582px;background:radial-gradient(ellipse at 50% 40%,#f3e3d6 0%,#d9c3c8 35%,#8f8c82 60%,#4f4b46 100%)" role="img" aria-label="Pastel bouquet with peach roses and lavender"></div>
  <p class="abs feature-lead" style="left:258px;top:582px">Solet iuvaret iudicabit nec ea, ne has enim propriae. Ex nec mazim imperdiet, decore nullam</p>
  <p class="abs feature-body" style="left:260px;top:649px">Solet iuvaret iudicabit nec ea, ne has enim propriae. Ex nec mazim imperdiet, decore nullam repudiandae ut ius. Elitr tation quo et, no cum odio agam munere. No cum aeque aperiam, facer</p>
  <a class="btn abs" style="left:257px;top:794px" href="#">Read more</a>

  <h2 class="abs feature-title" style="left:467px;top:528px">Fugit Delicata Ei Mea Laudem</h2>
  <div class="abs feature-photo" style="left:466px;top:582px;background:radial-gradient(ellipse at 50% 35%,#f1dde0 0%,#c9b3a6 35%,#6f7a55 65%,#4a5a36 100%)" role="img" aria-label="Pink rose arrangement in a silver bowl on a wooden stool"></div>
  <p class="abs feature-lead" style="left:688px;top:582px">Solet iuvaret iudicabit nec ea, ne has enim propriae. Ex nec mazim imperdiet, decore nullam</p>
  <p class="abs feature-body" style="left:690px;top:649px">Solet iuvaret iudicabit nec ea, ne has enim propriae. Ex nec mazim imperdiet, decore nullam repudiandae ut ius. Elitr tation quo et, no cum odio agam munere. No cum aeque aperiam, facer</p>
  <a class="btn abs" style="left:687px;top:794px" href="#">Read more</a>
</section>

<footer class="abs site-footer">
  <div class="abs footer-rule"></div>
  <div class="abs footer-head" style="left:104px;color:var(--orange)">TELEPHONE NUMBERS</div>
  <div class="abs footer-head" style="left:336px;color:var(--green)">EMAIL ADDRESS</div>
  <div class="abs footer-head" style="left:558px;color:var(--pink);display:flex;gap:10px;align-items:center">FOLLOW US <span class="social"><span class="social-sq"></span>Chatterly</span></div>

  <div class="abs" style="left:104px;top:64px">
    <div class="footer-label">Central London</div><div class="footer-value">0203 554 2071</div>
    <div class="footer-label">Greater London</div><div class="footer-value">0208 417 2359</div>
    <div class="footer-label">Marlow</div><div class="footer-value">01628 570213</div>
    <div class="footer-label">Mobile</div><div class="footer-value">07845 190627</div>
  </div>
  <div class="abs" style="left:336px;top:64px">
    <div class="footer-label">Orders</div><div class="footer-value">orders@joandmiras.co.uk</div>
    <div class="footer-label">Customer Service</div><div class="footer-value">CS@joandmiras.co.uk</div>
  </div>
  <div class="abs" style="left:336px;top:170px">
    <div class="pay-head">WE ACCEPT</div>
    <div class="pay-grid">
      <div class="pay-card">PAYRO</div>
      <div class="pay-card">Cardwell</div>
      <div class="pay-card">Northern Swift</div>
      <div class="pay-card">Quikpay</div>
    </div>
  </div>
  <div class="abs" style="left:558px;top:70px">
    <div class="guild-head">MEMBER of<br>National Petal Guild</div>
    <div class="guild-badge" style="margin-top:6px"><div class="guild-mark"></div></div>
  </div>
</footer>

<div class="abs bottom-rule"></div>
<nav class="abs bottom-links">
  <a href="#">Classic Flowers</a><a href="#">Luxury Bouqets</a><a href="#">Platinum Collection</a><a href="#">Autumn Flowers</a><a href="#">Luxury Roses</a>
</nav>

</body>
</html>
```